KORBALT

The business want a professional looking business card. We have a scetch we will add but want the extra upgrade, and would like more suggestions for variations of our business cards.

```html
<!DOCTYPE html>
<html lang="en">
<head>
<meta charset="utf-8">
<title>KORBALT – Business Card Variations</title>
<link rel="stylesheet" href="https://fonts.googleapis.com/css2?family=Cinzel:wght@500;600&family=Montserrat:wght@400;500&display=swap">
<style>
  :root {
    --page: #efebe7;
    --beige: #ddd6cc;
    --olive-light: #4d4833;
    --olive-dark: #262619;
    --bronze: #74561f;
    --bronze-mid: #a8843d;
    --gold-light: #e4d281;
    --gold: #c7a04a;
    --gold-deep: #ad7d2c;
    --gold-pale: #efe0a0;
    --cream: #f5ecc4;
    --shadow: rgba(40, 30, 10, 0.35);
  }
  * { box-sizing: border-box; margin: 0; padding: 0; }
  html, body { width: 1200px; height: 1200px; overflow: hidden; }
  body { background: var(--page); position: relative; font-family: "Montserrat", Arial, sans-serif; }

  .card {
    position: absolute; width: 510px; height: 315px; overflow: hidden;
    box-shadow: 4px 6px 14px var(--shadow);
  }
  .card--beige { background: var(--beige); }
  .card--olive { background: linear-gradient(100deg, var(--olive-light) 0%, #37351f 55%, var(--olive-dark) 100%); }
  .card--gold { background: linear-gradient(100deg, var(--bronze) 0%, var(--bronze-mid) 45%, var(--gold-light) 100%); }

  .pos-a { left: 63px; top: 63px; }
  .pos-b { left: 618px; top: 60px; }
  .pos-c { left: 63px; top: 423px; }
  .pos-d { left: 618px; top: 430px; }
  .pos-e { left: 63px; top: 795px; }
  .pos-f { left: 618px; top: 795px; }

  /* faint edge decoration */
  .edge-mark {
    position: absolute; right: -70px; top: 60px; width: 170px; height: 170px;
    border-radius: 50%; opacity: 0.14;
  }
  .card--beige .edge-mark { background: var(--gold-deep); }
  .card--olive .edge-mark { background: var(--gold-light); opacity: 0.08; }
  .card--gold .edge-mark { background: var(--gold-light); opacity: 0.18; }

  /* brand block on front cards */
  .brand-front {
    position: absolute; left: 0; right: 0; top: 48px; text-align: center;
  }
  .brand-dot { display: block; margin: 0 auto; border-radius: 50%; }
  .brand-front .brand-dot { width: 92px; height: 92px; }
  .brand-name {
    font-family: "Cinzel", Georgia, serif; font-weight: 500; line-height: 1;
  }
  .brand-front .brand-name { font-size: 42px; letter-spacing: 7px; margin-top: 52px; padding-left: 7px; }
  .brand-since { font-family: "Montserrat", Arial, sans-serif; line-height: 1; }
  .brand-front .brand-since { font-size: 17px; letter-spacing: 5px; margin-top: 10px; padding-left: 5px; }

  /* colour per card */
  .tone-gold .brand-dot { background: var(--gold); }
  .tone-gold .brand-name, .tone-gold .brand-since { color: var(--gold); }
  .tone-light .brand-dot { background: var(--gold-light); }
  .tone-light .brand-name, .tone-light .brand-since { color: var(--gold-light); }

  /* back cards */
  .brand-back {
    position: absolute; left: 0; width: 240px; top: 84px; text-align: center;
  }
  .brand-back .brand-dot { width: 62px; height: 62px; }
  .brand-back .brand-name { font-size: 22px; letter-spacing: 3px; margin-top: 36px; padding-left: 3px; }
  .brand-back .brand-since { font-size: 9px; letter-spacing: 3px; margin-top: 5px; padding-left: 3px; }

  .holder { position: absolute; left: 235px; top: 40px; }
  .holder-name { font-family: "Cinzel", Georgia, serif; font-weight: 600; font-size: 20px; line-height: 1.1; }
  .holder-role { font-family: "Montserrat", Arial, sans-serif; font-size: 18px; letter-spacing: 1px; margin-top: 4px; }
  .holder-person { font-size: 11.5px; margin-top: 6px; }

  .contacts { position: absolute; left: 235px; top: 183px; list-style: none; }
  .contacts li { display: flex; align-items: center; height: 24.5px; font-size: 16.5px; }
  .contacts svg { width: 15px; height: 15px; margin-right: 8px; flex: none; }

  .ink-pale .holder-name { color: var(--gold-pale); }
  .ink-pale .holder-role, .ink-pale .contacts li { color: var(--cream); }
  .ink-pale .holder-person { color: var(--gold-pale); }
  .ink-pale .icon-bg { fill: var(--gold-pale); }
  .ink-pale .icon-fg { fill: var(--olive-dark); stroke: var(--olive-dark); }

  .ink-bright .holder-name, .ink-bright .holder-role, .ink-bright .holder-person,
  .ink-bright .contacts li { color: #fbf1bd; }
  .ink-bright .icon-bg { fill: #fbf1bd; }
  .ink-bright .icon-fg { fill: var(--bronze); stroke: var(--bronze); }

  .ink-deep .holder-name { color: var(--gold-deep); }
  .ink-deep .holder-role, .ink-deep .contacts li { color: var(--gold-deep); }
  .ink-deep .holder-person { color: var(--gold-deep); }
  .ink-deep .icon-bg { fill: var(--gold-deep); }
  .ink-deep .icon-fg { fill: var(--beige); stroke: var(--beige); }
</style>
</head>
<body>

<!-- front, beige -->
<section class="card card--beige pos-a tone-gold">
  <div class="edge-mark"></div>
  <div class="brand-front">
    <span class="brand-dot"></span>
    <p class="brand-name">KORBALT</p>
    <p class="brand-since">SINCE 2026</p>
  </div>
</section>

<!-- front, olive -->
<section class="card card--olive pos-b tone-light">
  <div class="edge-mark"></div>
  <div class="brand-front">
    <span class="brand-dot"></span>
    <p class="brand-name">KORBALT</p>
    <p class="brand-since">SINCE 2026</p>
  </div>
</section>

<!-- back, olive -->
<section class="card card--olive pos-c tone-light ink-pale">
  <div class="brand-back">
    <span class="brand-dot"></span>
    <p class="brand-name">KORBALT</p>
    <p class="brand-since">SINCE 2026</p>
  </div>
  <div class="holder">
    <p class="holder-name">KORBALT SOLVANG</p>
    <p class="holder-role">CEO &amp; FOUNDER</p>
    <p class="holder-person">Lars Henrik Solvang</p>
  </div>
  <ul class="contacts">
    <li><svg viewBox="0 0 16 16"><circle class="icon-bg" cx="8" cy="8" r="8"/><path class="icon-fg" stroke="none" d="M5.2 4h1.6l.8 2-1 .8a5 5 0 0 0 2.6 2.6l.8-1 2 .8v1.6c0 .5-.4.9-.9.9A7 7 0 0 1 4.3 4.9c0-.5.4-.9.9-.9z"/></svg>004791234567</li>
    <li><svg viewBox="0 0 16 16"><circle class="icon-bg" cx="8" cy="8" r="8"/><rect class="icon-fg" x="4" y="5" width="8" height="6" fill="none" stroke-width="1"/><path class="icon-fg" fill="none" stroke-width="1" d="M4 5l4 3.3L12 5"/></svg>korbalt.llc@mailhub.com</li>
    <li><svg viewBox="0 0 16 16"><circle class="icon-bg" cx="8" cy="8" r="8"/><path class="icon-fg" fill="none" stroke-width="0.9" d="M3 8h10M8 3c-2.2 2.8-2.2 7.2 0 10M8 3c2.2 2.8 2.2 7.2 0 10"/></svg>www.korbalt.llc</li>
  </ul>
</section>

<!-- back, gold -->
<section class="card card--gold pos-d tone-light ink-bright">
  <div class="brand-back">
    <span class="brand-dot"></span>
    <p class="brand-name">KORBALT</p>
    <p class="brand-since">SINCE 2026</p>
  </div>
  <div class="holder">
    <p class="holder-name">KORBALT SOLVANG</p>
    <p class="holder-role">CEO &amp; FOUNDER</p>
    <p class="holder-person">Lars Henrik Solvang</p>
  </div>
  <ul class="contacts">
    <li><svg viewBox="0 0 16 16"><circle class="icon-bg" cx="8" cy="8" r="8"/><path class="icon-fg" stroke="none" d="M5.2 4h1.6l.8 2-1 .8a5 5 0 0 0 2.6 2.6l.8-1 2 .8v1.6c0 .5-.4.9-.9.9A7 7 0 0 1 4.3 4.9c0-.5.4-.9.9-.9z"/></svg>004791234567</li>
    <li><svg viewBox="0 0 16 16"><circle class="icon-bg" cx="8" cy="8" r="8"/><rect class="icon-fg" x="4" y="5" width="8" height="6" fill="none" stroke-width="1"/><path class="icon-fg" fill="none" stroke-width="1" d="M4 5l4 3.3L12 5"/></svg>korbalt.llc@mailhub.com</li>
    <li><svg viewBox="0 0 16 16"><circle class="icon-bg" cx="8" cy="8" r="8"/><path class="icon-fg" fill="none" stroke-width="0.9" d="M3 8h10M8 3c-2.2 2.8-2.2 7.2 0 10M8 3c2.2 2.8 2.2 7.2 0 10"/></svg>www.korbalt.llc</li>
  </ul>
</section>

<!-- front, gold -->
<section class="card card--gold pos-e tone-light">
  <div class="edge-mark"></div>
  <div class="brand-front">
    <span class="brand-dot"></span>
    <p class="brand-name">KORBALT</p>
    <p class="brand-since">SINCE 2026</p>
  </div>
</section>

<!-- back, beige -->
<section class="card card--beige pos-f tone-gold ink-deep">
  <div class="brand-back">
    <span class="brand-dot"></span>
    <p class="brand-name">KORBALT</p>
    <p class="brand-since">SINCE 2026</p>
  </div>
  <div class="holder">
    <p class="holder-name">KORBALT SOLVANG</p>
    <p class="holder-role">CEO &amp; FOUNDER</p>
    <p class="holder-person">Lars Henrik Solvang</p>
  </div>
  <ul class="contacts">
    <li><svg viewBox="0 0 16 16"><circle class="icon-bg" cx="8" cy="8" r="8"/><path class="icon-fg" stroke="none" d="M5.2 4h1.6l.8 2-1 .8a5 5 0 0 0 2.6 2.6l.8-1 2 .8v1.6c0 .5-.4.9-.9.9A7 7 0 0 1 4.3 4.9c0-.5.4-.9.9-.9z"/></svg>004791234567</li>
    <li><svg viewBox="0 0 16 16"><circle class="icon-bg" cx="8" cy="8" r="8"/><rect class="icon-fg" x="4" y="5" width="8" height="6" fill="none" stroke-width="1"/><path class="icon-fg" fill="none" stroke-width="1" d="M4 5l4 3.3L12 5"/></svg>korbalt.llc@mailhub.com</li>
    <li><svg viewBox="0 0 16 16"><circle class="icon-bg" cx="8" cy="8" r="8"/><path class="icon-fg" fill="none" stroke-width="0.9" d="M3 8h10M8 3c-2.2 2.8-2.2 7.2 0 10M8 3c2.2 2.8 2.2 7.2 0 10"/></svg>www.korbalt.llc</li>
  </ul>
</section>

</body>
</html>
```